Varnel Solutions requires a new business card.

We are an online professional tool store.

Target Market(s)

We target the professional technician.

Industry/Entity Type

Business

Contact Information for Business Card

VarnelSolutions.com.au

sales@varnelsolutions.com

Requirements
Must have
• Needs to look commercial and professional
Should not have
• No Australian Colors, maps or shapes.
• No Shapes of Tools

```html
<!DOCTYPE html>
<html lang="en">
<head>
<meta charset="utf-8">
<title>Varnel Solutions – Business Card</title>
<link rel="stylesheet" href="https://fonts.googleapis.com/css2?family=Exo+2:wght@500;600&family=Roboto:wght@400&display=swap">
<style>
  :root {
    --backdrop: #262626;
    --card-white: #f3f3f3;
    --brand-blue: #0b23a9;
    --ink-blue: #1a2fb5;
    --accent-cyan: #1b95d2;
    --text-grey: #4e4e4e;
    --white: #ffffff;
  }
  * { margin: 0; padding: 0; box-sizing: border-box; }
  html, body { width: 1200px; height: 960px; overflow: hidden; }
  body { background: var(--backdrop); position: relative; font-family: "Roboto", Arial, sans-serif; }

  .card { position: absolute; width: 600px; height: 343px; overflow: hidden; }
  .card-front { left: 314px; top: 113px; background: var(--card-white); }
  .card-back { left: 311px; top: 472px; background: var(--brand-blue); }

  .brand { position: absolute; display: flex; align-items: center; gap: 12px; }
  .brand-dot { border-radius: 50%; flex: none; }
  .brand-name { font-family: "Exo 2", Arial, sans-serif; font-weight: 600; white-space: nowrap; line-height: 1; }

  .card-front .brand { left: 38px; top: 58px; }
  .card-front .brand-dot { width: 28px; height: 28px; background: var(--accent-cyan); }
  .card-front .brand-name { font-size: 27px; color: var(--ink-blue); }

  .address { position: absolute; left: 37px; top: 174px; font-size: 14.5px; line-height: 18px; color: var(--text-grey); }

  .contact-list { position: absolute; left: 37px; top: 220px; list-style: none; }
  .contact-list li { display: flex; align-items: center; height: 19px; font-size: 14.5px; color: var(--text-grey); }
  .contact-list svg { width: 15px; height: 14px; margin-right: 9px; fill: var(--ink-blue); flex: none; }

  .person { position: absolute; right: 46px; top: 226px; text-align: right; font-family: "Exo 2", Arial, sans-serif; }
  .person-name { font-size: 22px; font-weight: 600; color: var(--ink-blue); letter-spacing: 0.3px; line-height: 24px; }
  .person-role { font-size: 14px; font-weight: 500; color: var(--accent-cyan); letter-spacing: 0.5px; margin-top: 2px; }

  .card-back .brand { left: 50%; top: 146px; transform: translateX(-50%); gap: 16px; }
  .card-back .brand-dot { width: 40px; height: 40px; background: var(--white); }
  .card-back .brand-name { font-size: 38px; color: var(--white); }

  .web-address {
    position: absolute; left: 0; right: 0; top: 288px; text-align: center;
    font-size: 15px; letter-spacing: 3px; color: var(--white);
  }
</style>
</head>
<body>
  <section class="card card-front">
    <div class="brand">
      <span class="brand-dot"></span>
      <span class="brand-name">Varnel Solutions</span>
    </div>

    <p class="address">2914 Linden Court<br>Fairbrook, Oregon 51682</p>

    <ul class="contact-list">
      <li>
        <svg viewBox="0 0 16 16" aria-hidden="true"><path d="M3.5 1l2.6 3-1.4 1.8c.9 2 2.5 3.6 4.5 4.5L11 8.9l3 2.6-1.5 2.9C6.5 14.2 1.8 9.5 1.5 3.3z"/></svg>
        555 218 4307
      </li>
      <li>
        <svg viewBox="0 0 16 16" aria-hidden="true"><path d="M4.5 0h7a1 1 0 0 1 1 1v14a1 1 0 0 1-1 1h-7a1 1 0 0 1-1-1V1a1 1 0 0 1 1-1zm.8 2v10h5.4V2zM8 13a1 1 0 1 0 0 2 1 1 0 0 0 0-2z"/></svg>
        555 730 1946
      </li>
      <li>
        <svg viewBox="0 0 16 16" aria-hidden="true"><path d="M4 1h8v4H4zM1 6h14v7H1zm3 5h8v4H4z"/></svg>
        555 462 8813
      </li>
      <li>
        <svg viewBox="0 0 16 16" aria-hidden="true"><path d="M1 3h14v10H1zm1.5 1.5v.4L8 9l5.5-4.1v-.4z"/></svg>
        sales@varnelsolutions.com
      </li>
      <li>
        <svg viewBox="0 0 16 16" aria-hidden="true"><path d="M8 1a7 7 0 1 0 0 14A7 7 0 0 0 8 1zm0 1.6c.9 1.1 1.5 2.8 1.6 4.6H6.4C6.5 5.4 7.1 3.7 8 2.6zM6.4 8.8h3.2C9.5 10.6 8.9 12.3 8 13.4 7.1 12.3 6.5 10.6 6.4 8.8z"/></svg>
        VarnelSolutions.com.au
      </li>
    </ul>

    <div class="person">
      <div class="person-name">DANIEL HARWOOD</div>
      <div class="person-role">CEO/FOUNDER</div>
    </div>
  </section>

  <section class="card card-back">
    <div class="brand">
      <span class="brand-dot"></span>
      <span class="brand-name">Varnel Solutions</span>
    </div>
    <p class="web-address">www.VarnelSolutions.com.au</p>
  </section>
</body>
</html>
```